Naturkosmetikpraxis sucht Design
Der Designer konnte gut meine Vorstellungen umsetzen und das in kürzester Zeit. Eine super Leistung, vor allem da ich weiß, dass es mir oft schwerfällt, mich klar auszudrücken.
Zielgruppe
Kosmetikpraxis, alle Altersgruppen aber Fokus Best Ager, vorwiegend weiblich, naturverbundene Menschen, gesundheitsbewusste Menschen, gestresste
gefallen soll es Menschen mit Hautproblemen und welchen, die einfach entspannen möchten.
Menschen, die Individualität suchen - nicht preiswerte Masse.
Aufgabenstellung
natürliche Hautpflegekonzepte,
Sugaring-Enthaarung, Wellness-Massagen, Naturnagelpflege, Wimpernlifting, Micro-Needling mit Lifting Pen, Klangschalenmassage, Permanent MakeUp
- Text mit Öffnungszeiten im Anhang "Banner..."
Als Farbe mag ich sehr dunkles rot, geht aber auch als Hintergrundfarbe. Ist wohl Brombeer etwa r171, g22, b78. Es geht ja hier um einen Banner für das Hoftor als Holz an einem Fachwerkhaus.
Habe noch ein paar Fotos aus meinem Bestand beigefügt.
Anderes Bild natürlich auch o.k.
BILD: 48193527 Frau m. Freesie von Bildarix. Das anhängende Bild flieder bluete 71846302 geht in eine ganz andere Richtung, ich weiß. Aber es ist ein tolles Bild und ich wäre durchaus bereit, auf flieder im Design zu wechseln. 08.04.14: jetzt hat sich das LOGO doch verändert.

```html
<!DOCTYPE html>
<html lang="de">
<head>
<meta charset="utf-8">
<title>Vitaflor Kosmetikpraxis – Banner</title>
<link rel="stylesheet" href="https://fonts.googleapis.com/css2?family=Arimo:wght@400&family=Raleway:wght@200&display=swap">
<style>
  :root {
    --pink: #e2268f;
    --pink-light: #ec4aa3;
    --pink-deep: #d01d80;
    --yellow: #e6c83c;
    --yellow-light: #ecd55a;
    --berry: #7c1246;
    --berry-deep: #5e0c35;
    --berry-text: #f2bcd6;
    --white: #ffffff;
    --skin-light: #f1ddc8;
    --skin-mid: #d9ad8f;
    --skin-dark: #a97a63;
  }
  html, body {
    margin: 0;
    padding: 0;
    width: 1200px;
    height: 2794px;
    overflow: hidden;
    background: var(--white);
  }
  .banner {
    position: relative;
    width: 1200px;
    height: 2794px;
    overflow: hidden;
    font-family: "Arimo", Arial, sans-serif;
    color: var(--white);
  }
  .brand-band {
    position: absolute;
    left: 0; top: 0;
    width: 1200px; height: 386px;
    background: linear-gradient(135deg, var(--pink-light) 0%, var(--pink) 45%, var(--pink-deep) 100%);
  }
  .brand {
    position: absolute;
    left: 0; right: 0; top: 70px;
    display: flex;
    align-items: center;
    justify-content: center;
    gap: 40px;
  }
  .brand-dot {
    width: 150px; height: 150px;
    border-radius: 50%;
    border: 6px solid var(--white);
    box-sizing: border-box;
  }
  .brand-name {
    font-family: "Arimo", Arial, sans-serif;
    font-weight: 400;
    color: var(--white);
    line-height: 1;
  }
  .brand-name .word {
    display: block;
    font-size: 120px;
    letter-spacing: 2px;
  }
  .brand-name .sub {
    display: block;
    font-size: 38px;
    letter-spacing: 6px;
    margin-top: 14px;
    text-align: right;
  }
  .name-band {
    position: absolute;
    left: 0; top: 386px;
    width: 1200px; height: 208px;
    background: linear-gradient(90deg, var(--yellow) 0%, var(--yellow-light) 50%, var(--yellow) 100%);
  }
  .owner-name {
    position: absolute;
    left: 0; right: 0; top: 60px;
    margin: 0;
    text-align: center;
    font-family: "Raleway", Arial, sans-serif;
    font-weight: 200;
    font-size: 96px;
    letter-spacing: 12px;
    line-height: 1;
    color: var(--white);
  }
  .pointer {
    position: absolute;
    left: 576px;
    width: 0; height: 0;
    border-left: 24px solid transparent;
    border-right: 24px solid transparent;
    z-index: 3;
  }
  .pointer-brand { top: 386px; border-top: 22px solid var(--pink-deep); }
  .pointer-name { top: 594px; border-top: 22px solid var(--yellow); }
  .pointer-services { top: 2280px; border-top: 22px solid var(--pink); }
  .portrait {
    position: absolute;
    left: 0; top: 594px;
    width: 1200px; height: 986px;
    background: radial-gradient(ellipse at 50% 45%, var(--skin-light) 0%, var(--skin-mid) 55%, var(--skin-dark) 100%);
  }
  .services-band {
    position: absolute;
    left: 0; top: 1580px;
    width: 1200px; height: 700px;
    background: linear-gradient(160deg, var(--pink-light) 0%, var(--pink) 50%, var(--pink-deep) 100%);
  }
  .services {
    list-style: none;
    margin: 0;
    padding: 0;
    position: absolute;
    left: 0; right: 0; top: 70px;
    text-align: center;
    font-size: 46px;
    line-height: 74px;
    letter-spacing: 0.5px;
  }
  .info-band {
    position: absolute;
    left: 0; top: 2280px;
    width: 1200px; height: 514px;
    background: linear-gradient(150deg, var(--berry) 0%, var(--berry-deep) 100%);
    text-align: center;
  }
  .hours {
    position: absolute;
    left: 0; right: 0; top: 80px;
    color: var(--berry-text);
    font-size: 29px;
    line-height: 48px;
  }
  .hours p { margin: 0; }
  .divider {
    position: absolute;
    left: 260px; top: 282px;
    width: 680px; height: 2px;
    background: rgba(255, 255, 255, 0.15);
  }
  .contact {
    position: absolute;
    left: 0; right: 0; top: 314px;
    color: var(--berry-text);
  }
  .contact p { margin: 0; }
  .contact .phone {
    font-size: 46px;
    line-height: 60px;
  }
  .contact .web {
    font-size: 30px;
    line-height: 44px;
    color: var(--white);
  }
</style>
</head>
<body>
<div class="banner">
  <header class="brand-band">
    <div class="brand">
      <div class="brand-dot"></div>
      <div class="brand-name">
        <span class="word">Vitaflor</span>
        <span class="sub">KOSMETIKPRAXIS</span>
      </div>
    </div>
  </header>
  <div class="pointer pointer-brand"></div>

  <section class="name-band">
    <h1 class="owner-name">LENA MARBERG</h1>
  </section>
  <div class="pointer pointer-name"></div>

  <div class="portrait" role="img" aria-label="Porträtfoto einer Frau mit klarer, gepflegter Haut"></div>

  <section class="services-band">
    <ul class="services">
      <li>KOSMETISCHE BEHANDLUNGEN</li>
      <li>PROBLEMHAUTPFLEGE</li>
      <li>SUGARING-ENTHAARUNG</li>
      <li>WELLNESS-MASSAGEN</li>
      <li>MICRO-NEEDLING LIFTING</li>
      <li>MANIKÜRE</li>
      <li>PERMANENT MAKEUP</li>
      <li>BERATUNG UND VERKAUF</li>
    </ul>
  </section>
  <div class="pointer pointer-services"></div>

  <footer class="info-band">
    <div class="hours">
      <p>Öffnungszeiten</p>
      <p>MO 15 - 19 Uhr nur Verkauf - DI, MI, FR 9.30 - 13 Uhr, 14 - 18 Uhr</p>
      <p>DO 14 - 20 Uhr SA 10 - 13 Uhr</p>
    </div>
    <div class="divider"></div>
    <div class="contact">
      <p class="phone">Tel. 06231 408752</p>
      <p class="web">www.kosmetikpraxis-marberg.de</p>
      <p class="web">info@vitaflor-kosmetik.de</p>
    </div>
  </footer>
</div>
</body>
</html>
```